Kestrel Vitality a Centre Pty Ltd

Business card is to promote and represent our new business. It's situated in
47 Fenwick Road
Elmvale 2199 Sydney
Our clinic is all about getting people back to great health giving them back their lifestyle in half the usual time it takes to get results elsewhere , we do this through innovative therapies with latest state of the art equipment ,skills ,knowledge and experience.
We give them back their pain free healthy lifestyle with lots of energy to love life and perform their best Quickly and effectively .
The final design should communicate
Trust , confidence, results .
Updates

Reason: Waiting for some designers to submit work Thanks

Target Market(s)

High end clients that take their health and results seriously ,
High end athletes , as well as general people that want to see results with different
Treatment Methods and approach

Industry/Entity Type

Clinic

Contact Information for Business Card

Kestrel Vitality Centre Pty Ltd
47 Fenwick Road Elmvale 2199 Sydney
Website www.kestrelvitalitycentre.com.au

Font styles to use
Other font styles liked:
• Gothic font medium

Requirements
Must have
• A designe that makes people look twice with a wow factor , a designe that isn't like all the rest .
• Must have the logo in the colours Iv provided in my files
• Must communicate Trust, confidence , results
Nice to have
• 1) The logo raised up or
• 2) Maybe a pop up logo on the card ?
• Or let's be creative and have two cards one on top of the other so the two cards slide .... The front will have the kestrel logo with the address details etc
• The other card with have
• eg your next app .......................................repeating all way down the card
Should not have
• Basic plain looking card that everyone else has

```html
<!DOCTYPE html>
<html lang="en">
<head>
<meta charset="utf-8">
<title>Kestrel Vitality Centre – Business Card</title>
<link href="https://fonts.googleapis.com/css2?family=Montserrat:wght@600&family=Roboto+Condensed:wght@300;400;700;800&family=Open+Sans:wght@400&display=swap" rel="stylesheet">
<style>
  :root {
    --backdrop: #e6e7e8;
    --card: #ffffff;
    --panel-grey: #efefef;
    --brand-green: #6abf45;
    --brand-navy: #23307a;
    --ink: #111111;
    --ink-soft: #444444;
    --rule-green: #8fd06a;
  }
  * { box-sizing: border-box; margin: 0; padding: 0; }
  html, body {
    width: 1200px; height: 1200px; overflow: hidden;
    background: var(--backdrop);
  }
  .canvas {
    position: relative; width: 1200px; height: 1200px;
    display: flex; flex-direction: column; align-items: center; justify-content: center; gap: 60px;
  }
  .card {
    position: relative; width: 880px; height: 503px;
    background: var(--card);
    box-shadow: 0 6px 18px rgba(0,0,0,0.18);
    overflow: hidden;
  }
  .card__shapes { position: absolute; inset: 0; width: 100%; height: 100%; }

  /* Brand name lockup */
  .brand {
    position: absolute; display: flex; align-items: center; gap: 18px;
    font-family: "Montserrat", sans-serif; font-weight: 600;
    color: var(--brand-navy); white-space: nowrap;
  }
  .brand__dot { border-radius: 50%; background: var(--brand-green); flex: none; }
  .card--front .brand {
    left: 50%; top: 50%; transform: translate(-50%, -50%);
    font-size: 48px;
  }
  .card--front .brand__dot { width: 64px; height: 64px; }
  .card--back .brand { left: 40px; top: 50px; font-size: 34px; }
  .card--back .brand__dot { width: 46px; height: 46px; }

  /* Contact details */
  .details__name {
    position: absolute; left: 470px; top: 200px;
    font-family: "Roboto Condensed", sans-serif; font-weight: 800;
    font-size: 30px; color: var(--ink); letter-spacing: 0.5px; text-transform: uppercase;
    white-space: nowrap;
  }
  .details__address {
    position: absolute; left: 470px; top: 236px;
    font-family: "Roboto Condensed", sans-serif; font-weight: 300;
    font-size: 25px; color: var(--ink); text-transform: uppercase;
    border-bottom: 2px solid var(--ink-soft); padding-bottom: 1px; line-height: 1.05;
    white-space: nowrap;
  }
  .contact__label {
    position: absolute; font-family: "Open Sans", sans-serif; font-size: 15px; color: var(--ink-soft);
    white-space: nowrap;
  }
  .contact__label--phone { right: 100px; top: 304px; }
  .contact__label--web { left: 470px; top: 346px; }
</style>
</head>
<body>
<main class="canvas">

  <section class="card card--front" aria-label="Business card front">
    <div class="brand"><span class="brand__dot"></span>Kestrel Vitality Centre</div>
  </section>

  <section class="card card--back" aria-label="Business card back">
    <svg class="card__shapes" viewBox="0 0 880 503" aria-hidden="true">
      <polygon points="455,185 880,185 880,503 262,503" fill="var(--panel-grey)"/>
      <polygon points="0,185 420,185 225,503 0,503" fill="var(--brand-green)"/>
      <line x1="500" y1="330" x2="805" y2="330" stroke="var(--rule-green)" stroke-width="2"/>
      <line x1="470" y1="372" x2="805" y2="372" stroke="var(--rule-green)" stroke-width="2"/>
      <g transform="translate(835 330)">
        <polygon points="-22,0 -11,-19 11,-19 22,0 11,19 -11,19" fill="var(--brand-green)"/>
        <path d="M-10,-3 q10,-8 20,0 v4 h-5 v-3 q-5,-2 -10,0 v3 h-5z" fill="#fff"/>
        <rect x="-7" y="2" width="14" height="8" rx="1.5" fill="#fff"/>
      </g>
      <g transform="translate(835 392)">
        <polygon points="-22,0 -11,-19 11,-19 22,0 11,19 -11,19" fill="var(--brand-green)"/>
        <rect x="-10" y="-8" width="20" height="13" rx="1" fill="none" stroke="#fff" stroke-width="2.2"/>
        <line x1="-5" y1="9" x2="5" y2="9" stroke="#fff" stroke-width="2.2"/>
      </g>
    </svg>

    <div class="brand"><span class="brand__dot"></span>Kestrel Vitality Centre</div>

    <div class="details__name">Kestrel Vitality Centre</div>
    <div class="details__address">47 Fenwick Elmvale 2199 Sydney</div>
    <div class="contact__label contact__label--phone">youre phone</div>
    <div class="contact__label contact__label--web">www.kestrelvitalitycentre.com.au</div>
  </section>

</main>
</body>
</html>
```